Best website on the WWW

I am looking to create a multi tab wesbite to revamp our outdated website.

Here is an example of a companies website I really like
https://brambleforkhaulers.example/
Updates

Target Market(s)

New customers, government agency's

Industry/Entity Type

Auto repair, towing and recovery, hazmat clean up

Coding

Coded - Design and coding required

Number of Pages Required

5+ page

Font styles to use
Sans Serif

Requirements
Nice to have
• I would like to see an interactive website, that includes details and photos from our companies

```html
<!DOCTYPE html>
<html lang="en">
<head>
<meta charset="utf-8">
<title>Swift Harbor Repair &amp; Towing</title>
<link href="https://fonts.googleapis.com/css2?family=Barlow:wght@400;500;600;700;800&display=swap" rel="stylesheet">
<style>
:root{
  --navy:#173a84;
  --navy-deep:#0f2a66;
  --red:#a5123a;
  --ink:#222;
  --grey:#e6e6e6;
  --dark:#1f2226;
  --white:#fff;
}
*{margin:0;padding:0;box-sizing:border-box}
html,body{width:1200px;height:4691px;overflow:hidden}
body{font-family:'Barlow',sans-serif;color:var(--ink);background:var(--white);position:relative}
.abs{position:absolute}
.photo{position:absolute}

/* header */
.site-header{position:absolute;left:0;top:0;width:1200px;height:113px;background:var(--white)}
.brand{position:absolute;left:118px;top:30px;display:flex;align-items:center;gap:10px}
.brand-dot{width:40px;height:40px;border-radius:50%;background:var(--navy)}
.brand-name{font-weight:800;font-size:24px;color:var(--navy);text-transform:uppercase;line-height:1}
.quote-btn{position:absolute;left:630px;top:11px;width:177px;height:36px;border-radius:18px;background:var(--red);color:#fff;font-size:12px;font-weight:700;display:flex;align-items:center;justify-content:center}
.call{position:absolute;left:829px;top:17px;font-size:16px;color:var(--navy);display:flex;align-items:center;gap:6px}
.call b{font-weight:700}
.nav{position:absolute;left:320px;top:74px;display:flex;font-size:13px;font-weight:700;color:var(--navy)}
.nav a{color:inherit;text-decoration:none;padding:0 24px;border-left:1px solid #bbb;line-height:14px}
.nav a:first-child{border-left:none;color:var(--red)}
.nav-active{position:absolute;left:318px;top:108px;width:52px;height:4px;background:var(--red)}

/* hero */
.hero{position:absolute;left:0;top:113px;width:1200px;height:683px;overflow:hidden}
.hero-photo{position:absolute;inset:0;background:linear-gradient(100deg,#163a85 0%,#2c4f8f 35%,#7b8ba4 65%,#bfc6d0 100%)}
.hero-kicker{position:absolute;left:122px;top:222px;color:#fff;font-size:21px;font-weight:500;letter-spacing:.5px}
.hero-title{position:absolute;left:118px;top:252px;color:#fff;font-size:52px;font-weight:700;line-height:54px}
.hero-shapes{position:absolute;left:0;top:0}
.scroll-btn{position:absolute;left:578px;top:711px;width:54px;height:54px;border-radius:50%;background:#fff;box-shadow:0 2px 10px rgba(0,0,0,.15);display:flex;align-items:center;justify-content:center}

/* section headings */
.ghost{position:absolute;left:0;width:1200px;text-align:center;font-size:76px;font-weight:800;color:#f0f0f0;letter-spacing:2px;line-height:1}
.sec-title{position:absolute;left:0;width:1200px;text-align:center;font-size:40px;font-weight:700;color:var(--navy);line-height:1}
.sec-title .hl{color:var(--red)}
.rule{position:absolute;height:3px;width:64px;background:var(--red)}

/* services */
.svc{position:absolute;top:947px;height:273px;width:318px}
.svc-label{position:absolute;left:0;bottom:0;width:100%;height:55px;display:flex;align-items:center;justify-content:center;gap:12px;color:#fff;font-weight:700;font-size:19px}
.svc-featured{position:absolute;left:455px;top:1098px;width:297px;height:177px;background:var(--red);color:#fff;text-align:center;padding-top:18px}
.svc-featured h3{font-size:18px;font-weight:700;margin-top:10px}
.svc-featured p{font-size:11.5px;line-height:18px;margin:6px 22px 0}
.pill{display:inline-block;border:1.5px solid #fff;border-radius:16px;font-size:9px;font-weight:700;padding:6px 24px;margin-top:10px}

/* about */
.about{position:absolute;left:0;top:1338px;width:1200px;height:576px;background:var(--navy);overflow:hidden}
.about .photo{left:0;top:0;width:1200px;height:576px;background:linear-gradient(135deg,#3b3f47,#1b1d22 55%,#6a6f78);clip-path:polygon(710px 0,1200px 0,1200px 576px,483px 576px)}
.about-ghost{position:absolute;left:117px;top:100px;font-size:62px;font-weight:800;color:rgba(255,255,255,.06);line-height:1}
.about h2{position:absolute;left:117px;top:130px;color:#fff;font-size:33px;font-weight:700}
.about p{position:absolute;left:117px;width:390px;color:#fff;font-size:16.5px;line-height:27px}
.outline-btn{position:absolute;left:113px;top:394px;width:180px;height:45px;border:2px solid #fff;border-radius:23px;color:#fff;font-weight:700;font-size:14px;display:flex;align-items:center;justify-content:center}

/* features */
.feature-frame{position:absolute;border:5px solid var(--grey);background:#fff}
.feature-text{position:absolute;width:420px;text-align:center}
.feature-text h3{font-size:27px;font-weight:700;color:var(--red)}
.feature-text .mini-rule{width:48px;height:3px;background:var(--navy);margin:12px auto 18px}
.feature-text p{font-size:17.5px;line-height:27px;color:#333}
.accent-red{position:absolute;background:var(--red)}
.accent-navy{position:absolute;background:var(--navy)}
.feature-photo{position:absolute;width:453px;height:324px}

/* contact */
.contact{position:absolute;left:0;top:3642px;width:1200px;height:603px;background:var(--navy);overflow:hidden}
.contact .photo{left:0;top:0;width:1200px;height:603px;background:linear-gradient(160deg,#9ea3aa,#5a6069 50%,#2e3238);clip-path:polygon(0 0,483px 0,674px 603px,0 603px)}
.contact-ghost{position:absolute;left:685px;top:110px;font-size:50px;font-weight:800;color:rgba(255,255,255,.06);line-height:1}
.contact h2{position:absolute;left:685px;top:120px;color:#fff;font-size:33px;font-weight:700}
.c-item{position:absolute;left:692px;display:flex;gap:20px;color:#fff}
.c-icon{width:50px;height:50px;border-radius:50%;background:#fff;display:flex;align-items:center;justify-content:center;flex:none}
.c-item h4{font-size:16px;font-weight:700;margin-top:2px}
.c-item p{font-size:18px;line-height:26px}
.c-item .big{font-size:22px;font-weight:700}

/* footer */
.footer{position:absolute;left:0;top:4245px;width:1200px;height:446px;background:var(--dark);color:#fff}
.f-brand{position:absolute;left:118px;top:110px;display:flex;align-items:center;gap:10px}
.f-brand .brand-dot{background:#fff}
.f-brand .brand-name{color:#fff;font-size:28px}
.socials{position:absolute;left:152px;top:256px;display:flex;gap:12px}
.socials span{width:28px;height:28px;border-radius:50%;background:#fff}
.socials span:first-child{background:var(--red)}
.f-col{position:absolute;top:92px}
.f-col h4{font-size:15px;font-weight:700;padding-bottom:8px;border-bottom:1px solid #555;width:156px}
.f-links{list-style:none;margin-top:10px;font-size:12px;line-height:24.5px;color:#ddd}
.f-row{display:flex;gap:12px;font-size:11.5px;line-height:15px;color:#ddd;margin-top:14px}
.f-row .ico{width:16px;height:16px;border-radius:50%;background:#fff;flex:none}
.f-form{position:absolute;left:850px;top:92px;width:215px}
.f-form h4{font-size:15px;font-weight:700;margin-bottom:14px}
.field{background:#fff;color:#666;font-size:9px;height:22px;padding:5px 8px;margin-bottom:8px}
.field.tall{height:48px}
.send{background:var(--red);color:#fff;font-size:10px;font-weight:700;text-align:center;height:26px;line-height:26px;margin-top:6px}
.f-divider{position:absolute;left:0;top:371px;width:1200px;height:1px;background:#3a3d42}
.copyright{position:absolute;left:0;top:400px;width:1200px;text-align:center;font-size:11px;color:#bbb}
</style>
</head>
<body>

<header class="site-header">
  <div class="brand"><span class="brand-dot"></span><span class="brand-name">Swift Harbor</span></div>
  <div class="quote-btn">REQUEST A QUOTE</div>
  <div class="call">
    <svg width="18" height="18" viewBox="0 0 24 24"><path d="M6.6 10.8a15 15 0 006.6 6.6l2.2-2.2c.3-.3.7-.4 1-.2 1.1.4 2.3.6 3.6.6.6 0 1 .4 1 1V20c0 .6-.4 1-1 1A17 17 0 013 4c0-.6.4-1 1-1h3.5c.6 0 1 .4 1 1 0 1.3.2 2.5.6 3.6.1.3 0 .7-.2 1z" fill="#a5123a"/></svg>
    <span>CALL US <b>555-014-2290</b></span>
  </div>
  <nav class="nav"><a>HOME</a><a>ABOUT US</a><a>SERVICES</a><a>MONTHLY COUPONS</a><a>RESOURCES</a><a>CONTACT US</a></nav>
  <div class="nav-active"></div>
</header>

<section class="hero">
  <div class="hero-photo" role="img" aria-label="Heavy tow truck and pickup parked on a snowy roadside"></div>
  <div class="hero-kicker">SWIFT HARBOR REPAIR &amp; TOWING</div>
  <h1 class="hero-title">TOWING, AUTO &amp;<br>TRUCK REPAIR</h1>
  <svg class="hero-shapes" width="1200" height="683" viewBox="0 0 1200 683">
    <polygon points="0,552 605,627 0,683" fill="#a5123a"/>
    <polygon points="1200,515 605,627 1200,683" fill="#3a3d44"/>
    <polygon points="0,683 605,635 1200,683" fill="#fff"/>
  </svg>
</section>
<div class="scroll-btn">
  <svg width="22" height="26" viewBox="0 0 22 26"><path d="M11 2v21M3 15l8 8 8-8" stroke="#173a84" stroke-width="2" fill="none"/></svg>
</div>

<div class="ghost" style="top:826px">WHAT WE DO</div>
<h2 class="sec-title" style="top:858px">OUR SERVICES</h2>
<div class="rule" style="left:568px;top:904px"></div>

<div class="svc" style="left:113px">
  <div class="photo" style="inset:0;background:linear-gradient(180deg,#c9ccd2,#8d9097 60%,#6b5d4a)" role="img" aria-label="Tow truck towing a semi trailer"></div>
  <div class="svc-label" style="background:var(--navy)">
    <svg width="34" height="22" viewBox="0 0 34 22"><rect x="2" y="8" width="20" height="9" fill="none" stroke="#fff" stroke-width="2"/><path d="M22 10h6l4 4v3h-10z" fill="none" stroke="#fff" stroke-width="2"/><circle cx="8" cy="18" r="3" fill="#fff"/><circle cx="26" cy="18" r="3" fill="#fff"/></svg>
    TOWING SERVICES
  </div>
</div>
<div class="svc" style="left:444px">
  <div class="photo" style="inset:0;background:linear-gradient(180deg,#4a4f58,#23262b)" role="img" aria-label="Truck raised on a shop lift"></div>
</div>
<div class="svc-featured">
  <svg width="40" height="34" viewBox="0 0 40 34"><rect x="4" y="12" width="26" height="14" rx="2" fill="none" stroke="#fff" stroke-width="2"/><circle cx="11" cy="28" r="3" fill="#fff"/><circle cx="25" cy="28" r="3" fill="#fff"/><circle cx="32" cy="8" r="5" fill="none" stroke="#fff" stroke-width="2"/></svg>
  <h3>ROUTINE SERVICE</h3>
  <p>Our services are vital in maintaing your fuel efficiency and increasing the overall lifespan</p>
  <span class="pill">LEARN MORE</span>
</div>
<div class="svc" style="left:774px">
  <div class="photo" style="inset:0;background:linear-gradient(180deg,#6f7682,#cfd3d8 70%,#8a8f96)" role="img" aria-label="White pickup on a blue shop lift"></div>
  <div class="svc-label" style="background:#4b4e55">
    <svg width="26" height="26" viewBox="0 0 26 26"><circle cx="13" cy="13" r="9" fill="none" stroke="#fff" stroke-width="2" stroke-dasharray="4 2"/><circle cx="13" cy="13" r="4" fill="none" stroke="#fff" stroke-width="2"/></svg>
    REPAIRS SERVICES
  </div>
</div>

<section class="about">
  <div class="photo" role="img" aria-label="Black pickup truck on a lift inside the repair shop"></div>
  <svg class="abs" style="left:0;top:0" width="1200" height="576"><line x1="650" y1="130" x2="540" y2="576" stroke="#fff" stroke-width="3"/><polygon points="483,576 500,530 510,576" fill="#a5123a"/></svg>
  <div class="about-ghost">COMPANY</div>
  <h2>ABOUT SWIFT HARBOR</h2>
  <p style="top:198px">We now provide our customers with the ability to check their vehicle history on line!</p>
  <p style="top:257px">We will also send you email reminders when it is time to have your vehicle serviced according to your specific vehicle manufacture. Ask us how to get you registered today!</p>
  <div class="outline-btn">LEARN MORE</div>
</section>

<div class="ghost" style="top:1975px">WHY US?</div>
<h2 class="sec-title" style="top:2011px;font-size:35px">QUICK AND FRIENDLY <span class="hl">CUSTOMER SERVICE</span></h2>
<div class="rule" style="left:563px;top:2059px"></div>

<!-- feature 1 -->
<div class="feature-frame" style="left:118px;top:2110px;width:609px;height:436px"></div>
<div class="accent-red" style="left:613px;top:2163px;width:170px;height:30px"></div>
<div class="accent-navy" style="left:745px;top:2200px;width:341px;height:306px"></div>
<div class="feature-photo" style="left:621px;top:2172px;background:linear-gradient(135deg,#7a6a55,#2b2b2e 50%,#a09a92)" role="img" aria-label="Tire on a tire changing machine in the shop"></div>
<div class="feature-text" style="left:173px;top:2186px">
  <svg width="64" height="56" viewBox="0 0 64 56"><circle cx="32" cy="20" r="14" fill="none" stroke="#173a84" stroke-width="3"/><path d="M18 54c0-10 6-16 14-16s14 6 14 16" fill="none" stroke="#173a84" stroke-width="3"/><rect x="24" y="16" width="16" height="6" fill="#173a84"/></svg>
  <h3>EXPERIENCED TECHNICIANS</h3>
  <div class="mini-rule"></div>
  <p>The mechanics at our shop have over 60 years of experience between them. They are dedicated to providing high-quality repairs to keep you safe and happy.</p>
</div>

<!-- feature 2 -->
<div class="feature-frame" style="left:490px;top:2609px;width:606px;height:434px"></div>
<div class="accent-red" style="left:430px;top:2662px;width:170px;height:30px"></div>
<div class="accent-navy" style="left:130px;top:2700px;width:330px;height:306px"></div>
<div class="feature-photo" style="left:142px;top:2671px;width:450px;height:325px;background:linear-gradient(135deg,#b73340,#d8dde4 45%,#eef1f4)" role="img" aria-label="Tow truck recovering a vehicle in the snow"></div>
<div class="feature-text" style="left:637px;top:2690px">
  <svg width="60" height="56" viewBox="0 0 60 56"><circle cx="38" cy="18" r="14" fill="none" stroke="#173a84" stroke-width="3"/><text x="33" y="25" font-size="18" font-family="Barlow,sans-serif" font-weight="700" fill="#173a84">$</text><path d="M6 50V30h10l10 8h12" fill="none" stroke="#173a84" stroke-width="3"/></svg>
  <h3>COMPETITIVE PRICING</h3>
  <div class="mini-rule"></div>
  <p>Whether you're coming in for a routine inspection or a repair service, we promise that you will be completely satisfied with our work. We provide 24-month warranties with most of our services for your peace of mind.</p>
</div>

<!-- feature 3 -->
<div class="feature-frame" style="left:118px;top:3101px;width:609px;height:435px"></div>
<div class="accent-red" style="left:613px;top:3154px;width:170px;height:30px"></div>
<div class="accent-navy" style="left:745px;top:3192px;width:341px;height:306px"></div>
<div class="feature-photo" style="left:621px;top:3163px;background:linear-gradient(135deg,#2f5fb5,#1f2125 40%,#8d9199)" role="img" aria-label="Black truck raised on a blue lift in the service bay"></div>
<div class="feature-text" style="left:173px;top:3180px">
  <svg width="66" height="46" viewBox="0 0 66 46"><path d="M4 20l14-12 14 8 14-8 16 12-16 16-14-8-14 8z" fill="none" stroke="#173a84" stroke-width="3" stroke-linejoin="round"/></svg>
  <h3>OUR QUALITY PROMISE</h3>
  <div class="mini-rule"></div>
  <p>We're committed to providing a stress-free experience to both new and returning customers. Our shop only uses parts from reputable brands to ensure that your vehicle is always ready to drive.</p>
</div>

<section class="contact">
  <div class="photo" role="img" aria-label="Mechanic working on a dump truck in the shop"></div>
  <svg class="abs" style="left:0;top:0" width="1200" height="603"><line x1="488" y1="0" x2="679" y2="603" stroke="#a5123a" stroke-width="5"/></svg>
  <div class="contact-ghost">GET IN TOUCH</div>
  <h2>CONTACT US</h2>
  <div class="c-item" style="top:204px">
    <div class="c-icon"><svg width="20" height="26" viewBox="0 0 20 26"><path d="M10 1a9 9 0 019 9c0 7-9 15-9 15S1 17 1 10a9 9 0 019-9z" fill="#173a84"/><circle cx="10" cy="10" r="3.5" fill="#fff"/></svg></div>
    <div><h4>ADDRESS</h4><p>482 Larkspur Lane, Millbrook,<br>Ohio 40012, United States</p></div>
  </div>
  <div class="c-item" style="top:316px">
    <div class="c-icon"><svg width="22" height="22" viewBox="0 0 24 24"><path d="M6.6 10.8a15 15 0 006.6 6.6l2.2-2.2c.3-.3.7-.4 1-.2 1.1.4 2.3.6 3.6.6.6 0 1 .4 1 1V20c0 .6-.4 1-1 1A17 17 0 013 4c0-.6.4-1 1-1h3.5c.6 0 1 .4 1 1 0 1.3.2 2.5.6 3.6.1.3 0 .7-.2 1z" fill="#173a84"/></svg></div>
    <div><h4>PHONE NUMBER</h4><p class="big">555-014-2290</p></div>
  </div>
  <div class="c-item" style="top:404px">
    <div class="c-icon"><svg width="24" height="24" viewBox="0 0 24 24"><circle cx="12" cy="12" r="10" fill="#173a84"/><path d="M12 6v6l4 2" stroke="#fff" stroke-width="2" fill="none"/></svg></div>
    <div><h4>OPENING HOURS</h4><p>08:00 am – 01:00 pm</p></div>
  </div>
</section>

<footer class="footer">
  <div class="f-brand"><span class="brand-dot"></span><span class="brand-name">Swift Harbor</span></div>
  <div class="socials"><span></span><span></span><span></span><span></span></div>

  <div class="f-col" style="left:408px">
    <h4>QUICK LINKS</h4>
    <ul class="f-links"><li>Home</li><li>About Us</li><li>Our Services</li><li>Monthly Coupons</li><li>Reviews</li><li>Contact Us</li></ul>
  </div>

  <div class="f-col" style="left:610px">
    <h4 style="border:none">GET IN TOUCH</h4>
    <div class="f-row"><span class="ico"></span><span>482 Larkspur Lane,<br>Millbrook, Ohio 40012,<br>United States</span></div>
    <div class="f-row" style="font-size:15px;color:#fff"><span class="ico"></span><span>555-014-2290</span></div>
    <div class="f-row"><span class="ico"></span><span>hello@swiftharbor.example</span></div>
  </div>

  <div class="f-form">
    <h4>GET A QUOTE</h4>
    <div class="field">Name</div>
    <div class="field">Email address</div>
    <div class="field">Phone</div>
    <div class="field tall">Message</div>
    <div class="send">SEND MESSAGE</div>
  </div>

  <div class="f-divider"></div>
  <p class="copyright">Copyright © 2022 Swift Harbor Repair and Towing - All Rights Reserved.</p>
</footer>

</body>
</html>
```